Moderne Visitenkarten für Medizintechnikfirma
Zielgruppe
Vertriebsfirma von moderner und innovativer Medizintechnik
Zielgruppe: Ärzte, Kliniken, Medizintechnikfirmen, Patienten
Aufgabenstellung
Besonderes, modernes, auffälliges und ansprechendes Design ohne überladen oder aufdringlich zu sein
Farbenorientierung kann am Logo und der Website geschehen. Wenn zum Logo harmonierend, sind aber auch andere Farben gerne gesehen.
Format: eher horizontal, vertikal aber auch möglich, abgerundete Ecken einplanen
Wenn möglich folgende Infos bitte schon auf die Karten bringen (pro Person eine Karte):
Harald Zumbrink (CEO)
harald.zumbrink@vitalnova-partner.de
(VitalNova Partner GmbH
Lärchenstraße 14
49377 Fallrode)
www.vitalnova-partner.de
info@vitalnova-partner.de
Jannik Sprau (CoS)
jannik.sprau@vitalnova-partner.de
Die allgemeinen Firmeninfos können deutlich kleiner sein. Anschrift nur wenn es dadurch nicht zu viel werden würde.

```html
<!DOCTYPE html>
<html lang="de">
<head>
<meta charset="utf-8">
<title>VitalNova Partner – Visitenkarte</title>
<link href="https://fonts.googleapis.com/css2?family=Jost:wght@500;600&family=Carlito&display=swap" rel="stylesheet">
<style>
  :root {
    --backdrop: #e6e6e6;
    --card: #fafafa;
    --card-edge: #dcdcdc;
    --purple: #5a3f86;
    --orange: #e4502a;
  }
  * { margin: 0; padding: 0; box-sizing: border-box; }
  html, body { width: 1200px; height: 900px; overflow: hidden; }
  body { background: var(--backdrop); position: relative; font-family: "Carlito", "Calibri", sans-serif; color: var(--purple); }

  .card {
    position: absolute;
    top: 316px;
    width: 415px;
    height: 269px;
    background: var(--card);
    border: 1px solid var(--card-edge);
  }
  .card--front { left: 159px; }
  .card--back  { left: 620px; }

  .brand {
    position: absolute;
    left: 78px;
    top: 108px;
    display: flex;
    align-items: center;
    gap: 12px;
  }
  .brand__dot {
    width: 26px; height: 26px;
    border-radius: 50%;
    background: var(--purple);
  }
  .brand__name {
    font-family: "Jost", sans-serif;
    font-weight: 600;
    font-size: 25px;
    line-height: 1;
    color: var(--purple);
  }

  .person { position: absolute; left: 29px; top: 39px; }
  .person__name {
    font-family: "Jost", sans-serif;
    font-weight: 500;
    font-size: 20px;
    letter-spacing: 2.2px;
    line-height: 1;
  }
  .person__company { font-size: 12.5px; margin-top: 4px; letter-spacing: 0.3px; }
  .person__contact { margin-top: 12px; font-size: 12.5px; line-height: 17px; letter-spacing: 0.3px; }

  .company-info {
    position: absolute;
    left: 29px;
    top: 193px;
    display: flex;
    gap: 28px;
    font-size: 12.5px;
    line-height: 16px;
    letter-spacing: 0.3px;
  }
  .company-info__col { width: 170px; }
  .company-info__col + .company-info__col { width: 180px; }
</style>
</head>
<body>
  <section class="card card--front">
    <div class="brand">
      <span class="brand__dot"></span>
      <span class="brand__name">VitalNova Partner</span>
    </div>
  </section>

  <section class="card card--back">
    <div class="person">
      <h1 class="person__name">HARALD ZUMBRINK (CEO)</h1>
      <p class="person__company">VitalNova Partner GmbH</p>
      <p class="person__contact">
        harald.zumbrink@vitalnova-partner.de<br>
        Tel. +49 151 472 90 263
      </p>
    </div>
    <div class="company-info">
      <p class="company-info__col">Lärchenstraße 14, 49377 Fallrode<br>Tel. 0800 515 366 0</p>
      <p class="company-info__col">info@vitalnova-partner.de<br>www.vitalnova-partner.de</p>
    </div>
  </section>
</body>
</html>
```